WordPress WEB DESIGN & CODING for www.quelbrix-aerial.com Wireless Tower Contruction

WEB DESIGN & CODING for www.quelbrix-aerial.com
Wireless Tower Contruction Industry

SLOGAN: SERVICE AT A HIGHER LEVEL

Brannock Spires LLC has been in business since 2014 with combined professional Team experience of over 40 years.

Our Team is composed of long-time industry professionals in every aspect of the wireless telecommunications and commercial construction industries, including project management and site acquisition.

Brannock Spires specializes in providing tower installation services for the Wireless Telecommunications in the Southeastern of the United States.

Our key services are Wireless Tower Construction, Installation & Maintenance

Site audits and Tower mapping
Mount swaps and Modifications
Hardline & Jumper Installation
Antenna & Radio Install, Decom, Testing and Maintenance
Tower Lighting Installation & Testing
Fiber / Sweep / RET/ PIM Testing
Small Cells
Civil installation (concrete/steel platforms/electrical)
____________________________________________________________________

we need a clean yet vibrant, energetic website design that will convey our tower installation work to the fullest... It should use the navy and green colors of our logo and it must be mobile friendly and coded for both Android & IOS;
the site structure:
HOME
ABOUT
SERVICES
CONTRACT
CAREERS
GALLERY

I also attach a few pics we bought on shutterstock so these can be used if needed as we own them...

Target Market(s)

Client: large companies looking for general contractor or installation contractor in the market

Industry/Entity Type

Wireless Communication

Coding

Coded - Design and coding required

Number of Pages Required

4 page

Font styles to use
Sans Serif

Colors
0555a3
00a990
ffffff

Requirements
Must have
• Wordpress - must be both desktop mobile friendly and mobile is the key -
• should open swiftly on both Android & iOS
• See power point file with presentation about the company; page 5 is our keyservices but other contents can be used too
Nice to have
• panorama pics changing from the height/tower view showing the full overview, could be a slideshow or a short video...
Should not have
• flash animation does not work on iOS so this should be avoided.

```html
<!DOCTYPE html>
<html lang="en">
<head>
<meta charset="utf-8">
<title>Brannock Spires — Telecommunication Services</title>
<link href="https://fonts.googleapis.com/css2?family=Open+Sans:wght@400;600;700;800&display=swap" rel="stylesheet">
<style>
:root{
  --navy:#2f2a86;
  --navy-dark:#1f1c5c;
  --green:#3b8f3c;
  --ink:#222230;
  --muted:#6b6b78;
  --light:#f4f4f7;
  --white:#ffffff;
  --dark:#1c1c22;
  --grad:linear-gradient(90deg,var(--navy),var(--green));
}
*{box-sizing:border-box;margin:0;padding:0}
html,body{width:1200px;height:3968px;overflow:hidden}
body{font-family:"Open Sans",Arial,sans-serif;color:var(--ink);background:var(--white);position:relative}
.btn{display:inline-block;background:var(--grad);color:var(--white);font-size:10px;font-weight:700;letter-spacing:1px;padding:10px 22px;border-radius:3px;text-transform:uppercase}
.eyebrow{font-size:13px;font-weight:600;color:var(--ink);text-transform:uppercase;letter-spacing:.5px}
.title{font-size:34px;font-weight:800;color:var(--navy);text-transform:uppercase;line-height:1.1}
.center{text-align:center}
.ph{display:block}

/* top bar */
.topbar{height:28px;background:var(--navy);display:flex;justify-content:space-between;align-items:center;padding:0 150px;color:var(--white);font-size:10px}
.topbar .social{display:flex;gap:5px}
.topbar .social span{width:14px;height:14px;border-radius:50%;background:var(--white);opacity:.9}

/* header */
.header{height:92px;display:flex;align-items:center;justify-content:space-between;padding:0 150px}
.brand{display:flex;align-items:center;gap:10px;font-size:22px;font-weight:800;color:var(--navy)}
.brand i{width:18px;height:18px;background:var(--green);display:block}
.nav{display:flex;gap:6px;align-items:center}
.nav a{font-size:11px;font-weight:700;color:var(--ink);padding:9px 12px;text-decoration:none}
.nav a.active{background:var(--grad);color:var(--white);border-radius:2px}

/* hero */
.hero{position:relative;height:540px;background:linear-gradient(180deg,#5f6e86 0%,#b8c3d2 45%,#6b7a8e 100%);color:var(--white);text-align:center}
.hero .copy{position:absolute;top:170px;left:0;right:0}
.hero .kicker{font-size:14px;letter-spacing:4px;text-transform:uppercase}
.hero h1{font-size:52px;font-weight:700;margin:6px 0}
.hero .slogan{font-size:24px;letter-spacing:6px;font-weight:600;text-transform:uppercase;margin-bottom:26px}
.arrow{position:absolute;top:255px;width:32px;height:32px;background:var(--white);border-radius:4px;display:flex;align-items:center;justify-content:center}
.arrow.l{left:44px}.arrow.r{right:44px}
.dots{position:absolute;bottom:28px;left:0;right:0;display:flex;justify-content:center;gap:6px}
.dots span{width:7px;height:7px;border-radius:50%;background:rgba(255,255,255,.6)}
.dots span.on{background:var(--white)}
.hero .strip{position:absolute;bottom:0;left:0;right:0;height:6px;background:var(--grad)}

/* about */
.about{position:relative;height:500px}
.about .hex{position:absolute;left:160px;top:45px;width:300px;height:330px;clip-path:polygon(50% 0,100% 25%,100% 75%,50% 100%,0 75%,0 25%);background:radial-gradient(circle at 50% 40%,#f3c27a,#b0762c 55%,#3a2a1a)}
.about .badge{position:absolute;left:390px;top:320px;width:140px;height:140px;border-radius:50%;background:var(--white);box-shadow:0 4px 18px rgba(0,0,0,.18);display:flex;flex-direction:column;align-items:center;justify-content:center}
.badge b{font-size:40px;font-weight:800;line-height:1}
.badge small{font-size:9px;font-weight:700;text-transform:uppercase;text-align:center;line-height:1.3}
.about .text{position:absolute;left:575px;top:80px;width:470px}
.about h2{font-size:30px;font-weight:800;color:var(--navy);margin:4px 0 14px}
.about p{font-size:11px;line-height:1.7;color:var(--muted);margin-bottom:10px}
.about .actions{display:flex;align-items:center;gap:18px;margin-top:18px}
.phone{display:flex;align-items:center;gap:8px;font-size:11px;font-weight:700;color:var(--navy)}
.phone i{width:24px;height:24px;border-radius:50%;background:var(--green);display:flex;align-items:center;justify-content:center}
.about .tower{position:absolute;right:0;top:190px;width:150px;height:260px;background:linear-gradient(180deg,#f1f1f4,#dcdce3)}

/* services */
.services{height:540px;padding-top:20px}
.cards{display:flex;justify-content:center;gap:32px;margin-top:26px}
.card{width:264px;background:var(--white);box-shadow:0 2px 14px rgba(0,0,0,.12);text-align:center;padding-bottom:22px}
.card .img{height:180px;background:linear-gradient(160deg,#9aa9bb,#4a5a70)}
.card h3{font-size:11px;font-weight:800;margin:22px 0 10px;text-transform:uppercase}
.card p{font-size:10px;line-height:1.6;color:var(--muted);padding:0 32px;margin-bottom:16px}
.services .more{text-align:center;margin-top:40px}

/* how we work */
.how{position:relative;height:520px;background:linear-gradient(90deg,#2a2a30,#141418)}
.how .circle{position:absolute;left:70px;top:-20px;width:560px;height:560px;border-radius:50%;background:var(--white);box-shadow:0 0 0 10px rgba(255,255,255,.15);text-align:center;padding-top:50px}
.how h2{font-size:24px;font-weight:800;color:var(--navy);text-transform:uppercase}
.how .illo{width:300px;height:220px;margin:24px auto 20px;background:linear-gradient(160deg,#e8eef5,#b9c8da)}
.how p{font-size:10px;line-height:1.6;color:var(--muted);width:320px;margin:0 auto 22px}
.how .person{position:absolute;right:60px;top:20px;width:400px;height:500px;background:linear-gradient(180deg,#5a5a66,#2b2b35)}

/* why */
.why{position:relative;height:420px}
.why .text{position:absolute;left:160px;top:80px;width:400px}
.why .title{margin:2px 0 16px}
.why p{font-size:11px;line-height:1.7;color:var(--muted);margin-bottom:12px}
.why .media{position:absolute;left:640px;top:70px;width:460px;height:290px;background:linear-gradient(160deg,#dfe5ee,#8898b0)}
.play{position:absolute;left:50%;top:50%;width:56px;height:56px;margin:-28px 0 0 -28px;border-radius:50%;background:var(--dark);display:flex;align-items:center;justify-content:center}

/* team */
.team{height:480px;padding-top:30px}
.team .grid{display:flex;justify-content:center;gap:22px;margin-top:30px}
.member{width:200px;text-align:center}
.member .photo{height:240px;background:linear-gradient(180deg,#d9dbe0,#9ea3ad)}
.member .name{background:var(--navy);color:var(--white);padding:16px 0 14px}
.member .name b{display:block;font-size:12px;font-weight:700;text-transform:uppercase}
.member .name span{font-size:10px;opacity:.85}

/* cta */
.cta{height:132px;background:linear-gradient(90deg,#1d1d24,#3a3a45 60%,#1d1d24);display:flex;align-items:center;justify-content:space-between;padding:0 190px;color:var(--white)}
.cta h2{font-size:20px;font-weight:700;text-transform:uppercase}
.cta .btn{background:var(--white);color:var(--ink)}

/* reviews */
.reviews{height:368px;padding-top:60px;text-align:center}
.reviews .title{margin-bottom:36px}
.reviews p{font-size:13px;line-height:1.7;color:var(--ink);width:680px;margin:0 auto}
.reviewer{display:flex;justify-content:center;align-items:center;gap:10px;margin-top:24px}
.reviewer i{width:44px;height:44px;border-radius:50%;background:linear-gradient(160deg,#c8b7a6,#6d5a4a)}
.reviewer div{text-align:left;font-size:10px}
.reviewer b{display:block;font-size:11px}

/* footer */
.footer{height:300px;background:#0f0f14;color:#d8d8de;display:flex;gap:60px;padding:60px 160px 0}
.footer h4{font-size:11px;font-weight:800;color:var(--white);text-transform:uppercase;margin-bottom:12px}
.footer li{list-style:none;font-size:10px;line-height:2}
.footer .col{width:140px}
.footer .news{width:300px}
.footer .news p{font-size:10px;line-height:1.6;margin-bottom:12px}
.sub{display:flex}
.sub span{flex:1;background:var(--white);color:#888;font-size:10px;padding:9px 10px}
.sub b{background:var(--grad);color:var(--white);font-size:10px;padding:9px 14px}
.copy-bar{height:28px;background:var(--grad);color:var(--white);font-size:10px;display:flex;align-items:center;justify-content:center}
</style>
</head>
<body>

<div class="topbar">
  <span>(214) 555-0148 · Dallas, TX</span>
  <span>info@quelbrix-aerial.com</span>
  <span class="social"><span></span><span></span><span></span><span></span></span>
</div>

<header class="header">
  <div class="brand"><i></i>Brannock Spires</div>
  <nav class="nav">
    <a class="active">HOME</a><a>ABOUT US</a><a>SERVICES</a><a>GALLERY</a><a>CAREERS</a><a>CONTACT</a>
    <svg width="14" height="14" viewBox="0 0 14 14"><circle cx="6" cy="6" r="4.5" fill="none" stroke="#222230" stroke-width="1.6"/><line x1="9.3" y1="9.3" x2="13" y2="13" stroke="#222230" stroke-width="1.6"/></svg>
  </nav>
</header>

<section class="hero">
  <div class="ph" role="img" aria-label="Lattice telecom towers against a cloudy sky" style="position:absolute;inset:0"></div>
  <div class="copy">
    <div class="kicker">Brannock Spires</div>
    <h1>Telecommunication Services</h1>
    <div class="slogan">Service at a higher level</div>
    <span class="btn">Contact us</span>
  </div>
  <span class="arrow l"><svg width="10" height="12"><path d="M8 1 2 6l6 5" fill="none" stroke="#222" stroke-width="2"/></svg></span>
  <span class="arrow r"><svg width="10" height="12"><path d="M2 1l6 5-6 5" fill="none" stroke="#222" stroke-width="2"/></svg></span>
  <div class="dots"><span class="on"></span><span></span><span></span></div>
  <div class="strip"></div>
</section>

<section class="about">
  <div class="hex" role="img" aria-label="Tower lit from below at dusk"></div>
  <div class="badge"><b>40</b><small>Years<br>Experienced</small></div>
  <div class="text">
    <div class="eyebrow">About the company</div>
    <h2>BRANNOCK SPIRES</h2>
    <p>Brannock Spires LLC has been in business since 2014 with combined professional Team experience of over 40 years.</p>
    <p>Our Team is composed of long-time industry professionals in every aspect of the wireless telecommunications and commercial construction industries, including project management and site acquisition.</p>
    <p>Brannock Spires specializes in providing tower installation services for the Wireless Telecommunications in the Southeastern of the United States.</p>
    <div class="actions">
      <span class="btn">Discover more</span>
      <span class="phone"><i><svg width="12" height="12" viewBox="0 0 12 12"><path d="M3 1l2 2.5-1.2 1.3a7 7 0 0 0 3.4 3.4L8.5 7 11 9l-1 2C5 11 1 7 1 2z" fill="#fff"/></svg></i>(214) 555-0148</span>
    </div>
  </div>
  <div class="tower" role="img" aria-label="Red and white communication tower"></div>
</section>

<section class="services">
  <div class="eyebrow center">Our services</div>
  <h2 class="title center">Whats our offers</h2>
  <div class="cards">
    <div class="card"><div class="img" role="img" aria-label="Wireless tower under construction"></div><h3>Wireless Tower Construction</h3><p>New towers planned, raised and finished to spec, from ground work to top mount.</p><span class="btn">Learn more</span></div>
    <div class="card"><div class="img" role="img" aria-label="Technician installing antennas on a tower"></div><h3>Installation &amp; Maintenance</h3><p>Antenna and radio installs, mount swaps and routine upkeep at any height.</p><span class="btn">Learn more</span></div>
    <div class="card"><div class="img" role="img" aria-label="Fiber optic cable close-up"></div><h3>Fiber &amp; Sweep Testing</h3><p>Fiber, sweep, RET and PIM testing with clear reports for every site.</p><span class="btn">Learn more</span></div>
  </div>
  <div class="more"><span class="btn">View all</span></div>
</section>

<section class="how">
  <div class="circle">
    <h2>How we work</h2>
    <div class="illo" role="img" aria-label="Isometric illustration of a tower site and network"></div>
    <p>We survey the site, plan the build, install and test, then hand over a documented, ready network site.</p>
    <span class="btn">Read more</span>
  </div>
  <div class="person" role="img" aria-label="Smiling engineer holding a laptop"></div>
</section>

<section class="why">
  <div class="text">
    <div class="eyebrow">Our speciality</div>
    <h2 class="title">Why choose us?</h2>
    <p>Lorem ipsum dolor sit amet, consectetur adipiscing elit, sed do eiusmod tempor incididunt ut labore et dolore magna aliqua. Ut enim ad minim veniam, quis nostrud exercitation ullamco laboris nisi ut aliquip ex ea commodo consequat.</p>
    <p>Duis aute irure dolor in reprehenderit in voluptate velit esse cillum dolore eu fugiat nulla pariatur excepteur sint.</p>
    <span class="btn">Discover more</span>
  </div>
  <div class="media" role="img" aria-label="Laptop showing a video of telecom towers"><span class="play"><svg width="16" height="18"><path d="M2 1l13 8-13 8z" fill="#fff"/></svg></span></div>
</section>

<section class="team">
  <div class="eyebrow center">Our team</div>
  <h2 class="title center">Our best experts</h2>
  <div class="grid">
    <div class="member"><div class="photo" role="img" aria-label="Portrait of a team member"></div><div class="name"><b>Delia Marrow</b><span>Technician</span></div></div>
    <div class="member"><div class="photo" role="img" aria-label="Portrait of a team member"></div><div class="name"><b>Anders Pilkin</b><span>Technician</span></div></div>
    <div class="member"><div class="photo" role="img" aria-label="Portrait of a team member"></div><div class="name"><b>Marcus Edgell</b><span>Technician</span></div></div>
    <div class="member"><div class="photo" role="img" aria-label="Portrait of a team member"></div><div class="name"><b>Renata Vosk</b><span>Technician</span></div></div>
  </div>
</section>

<section class="cta">
  <h2>Looking an adequate solution for your project?</h2>
  <span class="btn">Let's talk</span>
</section>

<section class="reviews">
  <div class="eyebrow">Testimonial</div>
  <h2 class="title">Clients' reviews</h2>
  <p>Lorem ipsum dolor sit amet, consectetur adipiscing elit, sunt volupitate numquam culpa natus, maxime neque labore laudantium vel. Fugit sed dolorem sint dicta molestias, quam assumenda dignissimos rerum laborum nisi iure.</p>
  <p style="margin-top:10px">Sint voluptate numquam culpa natus, maxime neque.</p>
  <div class="reviewer"><i role="img" aria-label="Client avatar"></i><div><b>Hollis P. Arden</b>Site owner</div></div>
</section>

<footer class="footer">
  <div class="col"><h4>Quick links</h4><ul><li>Home</li><li>About Us</li><li>Services</li><li>Gallery</li><li>Careers</li><li>Contact</li></ul></div>
  <div class="col"><h4>Useful links</h4><ul><li>Privacy Policy</li><li>Terms &amp; Conditions</li><li>Help Center</li><li>Newsletter</li><li>Blog</li></ul></div>
  <div class="col" style="width:200px"><h4>Contact here</h4><ul><li>Brannock Spires LLC</li><li>418 Harlow Street</li><li>Dallas, TX 75207</li><li>Tel: (214) 555-0148</li><li>info@quelbrix-aerial.com</li></ul></div>
  <div class="news"><h4>Our newsletter</h4><p>Keep up to date with the latest news and tower projects from our crews.</p><div class="sub"><span>Enter your email</span><b>SUBSCRIBE</b></div></div>
</footer>
<div class="copy-bar">Copyright © 2024 Brannock Spires. All Rights Reserved.</div>

</body>
</html>
```